Graffiti Artist Business Card Design

I need a card with a Galaxy Background, a spray can in the foreground with a "super Nova ring" around it.

Business Name at top left
All personal details below on left

Have fun :)

Industry/Entity Type

Business

Contact Information for Business Card

Business Name: MURAL TIDEWAY
Name: Darrel Pikeman
Title: Head Graffiti Artist
Mobile: 0471 862 195
Email: brackfen_wu@mailpost-example.net
All types of designs from children's themes to detailed and huge! (Italic)

Requirements
Should not have
• Any logo's on the spray can unless you use Mural Tideway. Thanks

```html
<!DOCTYPE html>
<html lang="en">
<head>
<meta charset="utf-8">
<title>Mural Tideway – Business Card</title>
<link rel="stylesheet" href="https://fonts.googleapis.com/css2?family=Poiret+One&family=Philosopher:ital@1&display=swap">
<style>
  :root {
    --page-bg: #eeeeee;
    --space-deep: #1c2140;
    --space-mid: #3b3f78;
    --space-violet: #6b5fa8;
    --nebula-glow: #a9a3d8;
    --cap-light: #e6d3e4;
    --cap-pink: #b98fb6;
    --pill: rgba(24, 18, 32, 0.82);
    --text-light: #cfc8e6;
    --tagline-text: #e9e4f2;
  }
  * { margin: 0; padding: 0; box-sizing: border-box; }
  html, body {
    width: 1200px; height: 1000px; overflow: hidden;
    background: var(--page-bg);
  }
  .card {
    position: absolute; left: 50px; top: 165px;
    width: 1100px; height: 670px; overflow: hidden;
    background:
      radial-gradient(ellipse 40% 30% at 88% 25%, rgba(169,163,216,0.55), transparent 70%),
      radial-gradient(ellipse 45% 25% at 25% 55%, rgba(150,150,200,0.45), transparent 70%),
      radial-gradient(ellipse 70% 60% at 55% 35%, var(--space-violet), transparent 75%),
      linear-gradient(160deg, var(--space-deep) 0%, var(--space-mid) 55%, var(--space-deep) 100%);
  }
  .spray-cap {
    position: absolute; left: 430px; top: 110px;
    width: 620px; height: 560px;
    border-radius: 48% 48% 0 0 / 40% 40% 0 0;
    background:
      radial-gradient(ellipse 55% 22% at 50% 52%, rgba(255,240,250,0.85), transparent 70%),
      radial-gradient(ellipse 60% 45% at 50% 60%, var(--cap-pink), transparent 80%),
      linear-gradient(180deg, transparent 0%, var(--cap-light) 30%, rgba(210,190,210,0.7) 100%);
    opacity: 0.9;
  }
  .pill {
    position: absolute;
    background: var(--pill);
    border-radius: 40px;
    color: var(--text-light);
    font-family: "Poiret One", sans-serif;
  }
  .business-name {
    left: 40px; top: 36px; padding: 12px 34px;
    font-size: 54px; letter-spacing: 1px; white-space: nowrap;
  }
  .contact-details {
    left: 44px; top: 140px; width: 290px; padding: 16px 26px;
    font-size: 30px; line-height: 1.4; border-radius: 36px;
  }
  .email {
    left: 66px; top: 326px; padding: 10px 26px;
    font-size: 27px; white-space: nowrap;
  }
  .tagline {
    left: 34px; top: 455px; width: 1040px; padding: 16px 20px;
    font-family: "Philosopher", sans-serif; font-style: italic;
    font-size: 36px; color: var(--tagline-text); white-space: nowrap;
    text-align: center;
  }
</style>
</head>
<body>
  <main class="card" role="img" aria-label="Galaxy background with stars and blue-violet nebula clouds">
    <div class="spray-cap" role="img" aria-label="Spray can nozzle in the foreground surrounded by a glowing supernova ring"></div>
    <h1 class="pill business-name">MURAL TIDEWAY</h1>
    <div class="pill contact-details">
      <p class="contact-name">Darrel Pikeman</p>
      <p class="contact-title">Graffiti Artist</p>
      <p class="contact-phone">0471 862 195</p>
    </div>
    <p class="pill email">brackfen_wu@mailpost-example.net</p>
    <p class="pill tagline">All types of designs from children's themes to detailed and huge!</p>
  </main>
</body>
</html>
```